R7M Meridian Business Card Design

We need a business card created for our New Business "R7M Meridian"<br/><br/>The business card design is up to you however the following information must be on the business card:<br/><br/>Front of the business card -<br/>Email :dorianv@r7mmeridian.nz<br/>Mobile: +64 (0) 22 4871 659<br/>Website: www.r7mmeridian.nz<br/>Card Owner Name: Dorian Valcourt<br/>Company Title: Business Development Manager<br/>Slogan: "The BEST of both worlds". <br/>Logo On the front attached to the design brief<br/><br/>On the back: <br/>Space on the back for 4 more versions of the logo across the bottom of the card indicating different subsidiary brands - R7M Coffee, R7M Arts, R7M ?? (The card will be used for all of these brands - We Will add the extra subsidiary logos to the design once the design is finished (We are a graphics design team). <br/><br/>Other than that we want a premium feeling logo that remains universally usable depending on the business entity that we are using the card for. The use of bright bold colours would be great but we still want the card to feel premium.
Target Market(s)
Gift Design and Manufacturing Companies
Contact Information for Business Card
Front of the business card -
Email :dorianv@r7mmeridian.nz
Mobile: +64 (0) 22 4871 659
Website: www.r7mmeridian.nz
Card Owner Name: Dorian Valcourt
Company Title: Business Development Manager
Slogan: "The BEST of both worlds".
Logo On the front attached to the design brief

```html
<!DOCTYPE html>
<html lang="en">
<head>
<meta charset="utf-8">
<title>R7M Meridian Business Card</title>
<link href="https://fonts.googleapis.com/css2?family=Michroma&family=Open+Sans:wght@400;700&display=swap" rel="stylesheet">
<style>
  :root {
    --brand-blue: #3643a6;
    --brand-blue-light: #4550b0;
    --ink: #1f1f24;
    --charcoal: #2a2a2c;
    --paper: #ffffff;
    --backdrop: #2e2f31;
  }
  * { box-sizing: border-box; margin: 0; padding: 0; }
  html, body { width: 1200px; height: 900px; overflow: hidden; }
  body {
    background: var(--backdrop);
    font-family: "Open Sans", Arial, sans-serif;
    position: relative;
  }
  .card {
    position: absolute;
    left: 260px;
    width: 680px;
    height: 388px;
    border-radius: 22px;
    overflow: hidden;
  }
  /* Back side */
  .card--back {
    top: 48px;
    background: linear-gradient(135deg, var(--brand-blue) 0%, var(--brand-blue) 55%, var(--brand-blue-light) 100%);
    color: var(--paper);
  }
  .wordmark {
    display: flex;
    align-items: center;
    gap: 14px;
    font-family: "Open Sans", Arial, sans-serif;
    font-weight: 700;
    white-space: nowrap;
  }
  .wordmark__dot {
    border-radius: 50%;
    flex: none;
  }
  .card--back .wordmark {
    position: absolute;
    left: 0; right: 0;
    top: 130px;
    justify-content: center;
    font-size: 52px;
    letter-spacing: 1px;
    color: var(--paper);
  }
  .card--back .wordmark__dot {
    width: 30px; height: 30px;
    background: var(--paper);
  }
  .back-slogan {
    position: absolute;
    left: 0; right: 0;
    top: 310px;
    text-align: center;
    font-size: 19px;
    letter-spacing: 0.5px;
    color: var(--paper);
  }
  .back-slogan .arrow { font-size: 12px; vertical-align: 2px; margin: 0 8px; }
  .back-slogan strong { font-weight: 700; }

  /* Front side */
  .card--front {
    top: 470px;
    background: var(--paper);
  }
  .card--front .wordmark {
    position: absolute;
    left: 40px;
    top: 140px;
    font-size: 31px;
    color: var(--brand-blue);
    gap: 10px;
  }
  .card--front .wordmark__dot {
    width: 18px; height: 18px;
    background: var(--brand-blue);
  }
  .divider {
    position: absolute;
    left: 318px;
    top: 92px;
    width: 2px;
    height: 150px;
    background: var(--brand-blue);
  }
  .contact-block {
    position: absolute;
    left: 345px;
    top: 92px;
  }
  .holder-name {
    font-family: "Michroma", "Arial Black", sans-serif;
    font-size: 25px;
    font-weight: 400;
    color: var(--brand-blue);
    letter-spacing: 1px;
    -webkit-text-stroke: 0.8px var(--brand-blue);
  }
  .holder-role {
    font-size: 17px;
    color: var(--ink);
    margin-top: 2px;
    letter-spacing: 0.3px;
  }
  .contact-list {
    list-style: none;
    margin-top: 12px;
  }
  .contact-list li {
    display: flex;
    align-items: center;
    gap: 12px;
    font-size: 17px;
    color: var(--ink);
    line-height: 28px;
  }
  .contact-list svg { width: 15px; height: 15px; flex: none; }
  .card-footer {
    position: absolute;
    left: 0; bottom: 0;
    width: 680px; height: 80px;
  }
  .front-slogan {
    position: absolute;
    right: 46px;
    bottom: 16px;
    font-size: 19px;
    color: var(--paper);
    letter-spacing: 0.4px;
  }
  .front-slogan strong { font-weight: 700; }
</style>
</head>
<body>

<section class="card card--back" aria-label="Card back">
  <div class="wordmark">
    <span class="wordmark__dot"></span>
    <span class="wordmark__name">R7M Meridian</span>
  </div>
  <p class="back-slogan"><span class="arrow">&#9664;</span>The <strong>BEST</strong> of both worlds<span class="arrow">&#9654;</span></p>
</section>

<section class="card card--front" aria-label="Card front">
  <div class="wordmark">
    <span class="wordmark__dot"></span>
    <span class="wordmark__name">R7M Meridian</span>
  </div>

  <div class="divider"></div>

  <div class="contact-block">
    <h1 class="holder-name">DORIAN VALCOURT</h1>
    <p class="holder-role">Business Development Manager</p>
    <ul class="contact-list">
      <li>
        <svg viewBox="0 0 16 16" aria-hidden="true"><path d="M4 1.5 L6 4.5 L4.8 6 C5.6 8 7.8 10.4 10 11.2 L11.5 10 L14.5 12 L13 14.5 C7.5 14.5 1.5 8.5 1.5 3 Z" fill="none" stroke="#3643a6" stroke-width="1.4" stroke-linejoin="round"/></svg>
        +64 (0) 22 4871 659
      </li>
      <li>
        <svg viewBox="0 0 16 16" aria-hidden="true"><rect x="1.5" y="3.5" width="13" height="9" rx="1" fill="none" stroke="#3643a6" stroke-width="1.4"/><path d="M1.5 4 L8 9 L14.5 4" fill="none" stroke="#3643a6" stroke-width="1.4"/></svg>
        dorianv@r7mmeridian.nz
      </li>
      <li>
        <svg viewBox="0 0 16 16" aria-hidden="true"><circle cx="8" cy="8" r="6.5" fill="none" stroke="#3643a6" stroke-width="1.3"/><ellipse cx="8" cy="8" rx="3" ry="6.5" fill="none" stroke="#3643a6" stroke-width="1.1"/><path d="M1.5 8 H14.5 M2.6 4.6 H13.4 M2.6 11.4 H13.4" stroke="#3643a6" stroke-width="1.1"/></svg>
        www.r7mmeridian.nz
      </li>
    </ul>
  </div>

  <svg class="card-footer" viewBox="0 0 680 80" aria-hidden="true">
    <polygon points="0,54 350,80 0,80" fill="#3643a6"/>
    <polygon points="0,54 362,80 350,80" fill="#ffffff"/>
    <polygon points="356,80 394,26 680,26 680,80" fill="#2a2a2c"/>
  </svg>
  <p class="front-slogan">The <strong>BEST</strong> of both worlds</p>
</section>

</body>
</html>
```